Fresh Tarrow Work Post - Business Card Required

Dear All,

I own Velmira Limited, which in turn owns the website:
www.harbinworkpost.example

I want all of you wonderful creative people to come up with a slick, and awesome business card design that incorporates the logo on the site, and some colouring and design elements from it.

You have free reign in how you go about doing this, I won't be giving my contact details on this platform, but the winner will be asked to redesign based on my contact details which I will supply at the end.

I need the design to be completed within 5 days. I need the final print copies of the business cards by the 25th November, so unfortunately it's a bit of a rush to get these designs ready.

Any questions, please ask.

Thank you
Updates

Thank you all for your hard work and exceptional designs provided. I do have to pick one, so I have a very clear idea of which one this is, however I will wait one further day until the competition closes to be fair to all those have submitted, or are in the process of submitting. I wish you all the best and thank you again for your dedication.

```html
<!DOCTYPE html>
<html lang="en">
<head>
<meta charset="utf-8">
<title>Harbin Work Post – Business Card</title>
<link href="https://fonts.googleapis.com/css2?family=Cinzel:wght@500&family=Quicksand:wght@400;500&display=swap" rel="stylesheet">
<style>
  :root {
    --page: #e9e6e0;
    --gold: #c9a75a;
    --gold-light: #dcc088;
    --gold-deep: #9c7d3e;
    --ink: #221d16;
    --ink-soft: #2e271e;
    --night-top: #2f5ea8;
    --night-mid: #1b3460;
    --night-low: #141c2a;
    --text-muted: #b8a16c;
  }
  * { box-sizing: border-box; margin: 0; padding: 0; }
  html, body { width: 1200px; height: 900px; overflow: hidden; }
  body { background: var(--page); position: relative; font-family: "Quicksand", sans-serif; }

  .card {
    position: absolute; left: 280px; width: 640px; height: 366px;
    overflow: hidden; box-shadow: 0 6px 18px rgba(0,0,0,.25);
  }

  /* Front */
  .card--front { top: 46px; background: linear-gradient(180deg, var(--night-low) 0%, #0f151f 100%); }
  .card__skyline {
    position: absolute; inset: 0 0 120px 0;
    background: linear-gradient(180deg, var(--night-top) 0%, var(--night-mid) 55%, var(--night-low) 100%);
  }
  .brand-lockup {
    position: absolute; left: 0; right: 0; top: 232px;
    display: flex; flex-direction: column; align-items: center;
  }
  .brand-lockup__rule { width: 300px; height: 1px; background: var(--gold); }
  .brand-lockup__row { display: flex; align-items: center; gap: 12px; padding: 10px 0; }
  .brand-lockup__dot { width: 14px; height: 14px; border-radius: 50%; background: var(--gold); }
  .brand-lockup__name {
    font-family: "Cinzel", serif; font-weight: 500; font-size: 30px;
    letter-spacing: 3px; color: var(--gold);
  }

  /* Back */
  .card--back { top: 446px; }
  .card__texture {
    position: absolute; inset: 0;
    background: linear-gradient(120deg, var(--gold-deep) 0%, var(--gold-light) 50%, var(--gold) 100%);
  }
  .card__band {
    position: absolute; left: 0; right: 0; top: 150px; height: 118px; background: var(--ink);
  }
  .logo-box {
    position: absolute; left: 212px; top: 38px; width: 212px; height: 112px;
    background: var(--ink-soft); display: flex; align-items: center; justify-content: center; gap: 8px;
  }
  .logo-box__dot { width: 9px; height: 9px; border-radius: 50%; background: var(--gold); }
  .logo-box__name {
    font-family: "Cinzel", serif; font-weight: 500; font-size: 15px;
    letter-spacing: 1.5px; color: var(--gold);
  }
  .holder {
    position: absolute; left: 0; top: 222px; display: flex; align-items: center; gap: 14px;
  }
  .holder__mark { width: 52px; height: 30px; background: var(--gold); }
  .holder__name { font-size: 19px; font-weight: 500; color: var(--gold-light); line-height: 1; }
  .holder__title { font-size: 8px; color: var(--text-muted); letter-spacing: .5px; }

  .contact {
    position: absolute; left: 440px; top: 160px; height: 62px;
    border-left: 3px solid var(--gold); padding-left: 12px;
    list-style: none; display: flex; flex-direction: column; justify-content: space-between;
  }
  .contact__item { display: flex; align-items: center; gap: 6px; font-size: 7.5px; color: var(--text-muted); line-height: 1; }
  .contact__icon { width: 8px; height: 8px; fill: var(--gold); }
</style>
</head>
<body>

<section class="card card--front" aria-label="Business card front">
  <div class="card__skyline" role="img" aria-label="Night photograph of a riverside city skyline"></div>
  <div class="brand-lockup">
    <div class="brand-lockup__rule"></div>
    <div class="brand-lockup__row">
      <span class="brand-lockup__dot"></span>
      <span class="brand-lockup__name">HARBIN WORK POST</span>
    </div>
    <div class="brand-lockup__rule"></div>
  </div>
</section>

<section class="card card--back" aria-label="Business card back">
  <div class="card__texture" role="img" aria-label="Gold damask pattern background"></div>
  <div class="card__band"></div>

  <div class="logo-box">
    <span class="logo-box__dot"></span>
    <span class="logo-box__name">HARBIN WORK POST</span>
  </div>

  <div class="holder">
    <span class="holder__mark"></span>
    <div>
      <p class="holder__name">Dorian Halvek</p>
      <p class="holder__title">hiring director</p>
    </div>
  </div>

  <ul class="contact">
    <li class="contact__item">
      <svg class="contact__icon" viewBox="0 0 10 10"><path d="M2 0h2l1 2.5-1.3 1a5 5 0 0 0 2.8 2.8l1-1.3L10 6v2a2 2 0 0 1-2 2A8 8 0 0 1 0 2a2 2 0 0 1 2-2z"/></svg>
      000 444 555 666
    </li>
    <li class="contact__item">
      <svg class="contact__icon" viewBox="0 0 10 10"><path d="M0 2h10v6H0z M0 2l5 3.5L10 2" stroke="#221d16" stroke-width=".8"/></svg>
      contact@harbinworkpost.example
    </li>
    <li class="contact__item">
      <svg class="contact__icon" viewBox="0 0 10 10"><circle cx="5" cy="5" r="5"/></svg>
      www.harbinworkpost.example
    </li>
    <li class="contact__item">
      <svg class="contact__icon" viewBox="0 0 10 10"><path d="M5 0a3.5 3.5 0 0 1 3.5 3.5C8.5 6 5 10 5 10S1.5 6 1.5 3.5A3.5 3.5 0 0 1 5 0z"/></svg>
      12 Quay Lane, Tarrow, Harbin TW4 7QP
    </li>
  </ul>
</section>

</body>
</html>
```